Fashion Label Startup Business Card Design

Marianne Velk is a startup fashion designer based on the Gold Coast in QLD Australia. Mariannes label " Sorrina by Velk " is based upon taking old world design techniques and infusing them modern twist. The card design should incorporate an old world theme using colours like mustard, ocha, black, white and elements of lace pattern.

Card Details:

Marianne Velk
Fashion Designer
P: 04 0163 5271
E: sorrinabyvelk@mailbrook.net
W: www.threadpage.net/SOrrinaByVelk

```html
<!DOCTYPE html>
<html lang="en">
<head>
<meta charset="utf-8">
<title>Sorrina by Velk – Business Card</title>
<link rel="stylesheet" href="https://fonts.googleapis.com/css2?family=Tinos:wght@400;700&family=Libre+Baskerville:wght@400;700&display=swap">
<style>
  :root {
    --backdrop: #262626;
    --card-green: #4f8239;
    --card-green-deep: #3f6b2c;
    --watermark-green: #6b9440;
    --mustard: #fadc63;
    --gold-text: #f3d35c;
    --cream-text: #f0dc8a;
    --plate-black: #0d0d0b;
    --logo-green: #4c7f36;
  }
  * { box-sizing: border-box; margin: 0; padding: 0; }
  html, body { width: 1200px; height: 1000px; overflow: hidden; }
  body { background: var(--backdrop); position: relative; font-family: "Libre Baskerville", Georgia, serif; }

  .card {
    position: absolute;
    width: 640px;
    height: 390px;
    border-radius: 22px;
    background: var(--card-green);
    overflow: hidden;
    box-shadow: 0 10px 30px rgba(0,0,0,0.45);
  }

  /* Front */
  .card--front { left: 500px; top: 70px; }
  .front__band {
    position: absolute; left: 0; right: 0; top: 170px; height: 52px;
    background: var(--mustard);
  }
  .front__ornament {
    position: absolute; left: 150px; top: 70px; width: 340px; height: 250px;
    border-radius: 120px / 110px;
    background: radial-gradient(ellipse at center, #3a3212 0%, #1a1708 45%, #c9a93e 75%, #0b0b08 100%);
    box-shadow: 0 6px 14px rgba(0,0,0,0.4);
  }
  .front__plate {
    position: absolute; left: 205px; top: 140px; width: 230px; height: 110px;
    background: var(--plate-black);
    border: 3px solid var(--mustard);
    display: flex; align-items: center; justify-content: center;
  }
  .front__logo {
    font-family: "Tinos", "Times New Roman", serif;
    font-weight: 400; font-size: 32px; color: var(--logo-green);
    white-space: nowrap;
  }

  /* Back */
  .card--back { left: 100px; top: 520px; }
  .back__watermark {
    position: absolute; left: 28px; top: 18px;
    font-family: "Tinos", "Times New Roman", serif;
    font-weight: 400; font-size: 82px; line-height: 1;
    color: var(--watermark-green); white-space: nowrap;
  }
  .back__fold {
    position: absolute; left: 0; right: 0; height: 2px;
    background: var(--card-green-deep);
    box-shadow: 0 -3px 6px rgba(0,0,0,0.25);
  }
  .back__fold--upper { top: 148px; }
  .back__fold--lower { top: 262px; }
  .back__identity {
    position: absolute; left: 0; right: 0; top: 182px; text-align: center;
  }
  .back__name { font-weight: 700; font-size: 19px; color: var(--gold-text); }
  .back__role { font-size: 14px; color: var(--cream-text); margin-top: 2px; }
  .back__contact {
    position: absolute; left: 0; right: 0; top: 292px; text-align: center;
    list-style: none; font-size: 14px; color: var(--cream-text); line-height: 31px;
  }
</style>
</head>
<body>
  <section class="card card--front" aria-label="Card front">
    <div class="front__band"></div>
    <div class="front__ornament" role="img" aria-label="Ornate gold filigree scroll frame around the label name"></div>
    <div class="front__plate">
      <span class="front__logo">Sorrina by Velk</span>
    </div>
  </section>

  <section class="card card--back" aria-label="Card back">
    <div class="back__watermark">Sorrina by Velk</div>
    <div class="back__fold back__fold--upper"></div>
    <div class="back__fold back__fold--lower"></div>
    <div class="back__identity">
      <p class="back__name">Marianne Velk</p>
      <p class="back__role">Fashion Designer</p>
    </div>
    <ul class="back__contact">
      <li>04 0163 5271</li>
      <li>sorrinabyvelk@mailbrook.net</li>
      <li>www.threadpage.net/SOrrinaByVelk</li>
    </ul>
  </section>
</body>
</html>
```